依頼概要
■依頼の目的/概要
インフルエンザワクチンのポスターを作成して頂きたいです。
クリニック内の待合室に掲示します。

■依頼詳細
A2サイズです。
温かみのある柔らかいデザインをお願いします。
ポスターには、人のイラスト入りでお願いします。イラストはご自身で書いてくださってもいいですし、フリー素材でも構いません。
色合いは当院ホームページを参考にしてください。
当院ホームページ https://temuzeku.com/

記載する内容については、添付ファイルを参照してください。
ロゴデータは当選決定後に送らせて頂きます。

納品は、元データ(aiファイルやpsdファイル)とPNG書き出しでお願いします。

■重視する点
過去・現在までにデザインの経験のある方を希望致します。

その他何かご不明な点がございましたら、お気軽にご質問下さい。
よろしくお願いいたします。

文字が大きく読みやすい、温かみのあるデザインです。

皆さま、この度は当コンペにご参加いただき、誠にありがとうございます。
どれも力作で魅力的で選ぶのが大変でした。
今後ともどうぞよろしくお願いします。

```html
<!DOCTYPE html>
<html lang="ja">
<head>
<meta charset="utf-8">
<title>インフルエンザ予防接種</title>
<link href="https://fonts.googleapis.com/css2?family=M+PLUS+Rounded+1c:wght@400;500;700;800&display=swap" rel="stylesheet">
<style>
:root{
  --bg:#eaf5ef;
  --bg-soft:#f6fbf8;
  --teal:#2aa39a;
  --teal-dark:#1d8179;
  --mint:#a9dcc9;
  --blue-panel:#d9eef3;
  --ink:#3a4a48;
  --red:#e0473c;
  --white:#ffffff;
}
*{margin:0;padding:0;box-sizing:border-box}
html,body{width:846px;height:1200px;overflow:hidden}
body{font-family:"M PLUS Rounded 1c",sans-serif;color:var(--ink);background:var(--bg)}
.poster{position:relative;width:846px;height:1200px;background:linear-gradient(180deg,var(--bg-soft) 0%,var(--bg) 55%,#dff1e8 100%);overflow:hidden}
.clinic-name{position:absolute;top:28px;right:40px;font-size:22px;font-weight:700;color:var(--ink);letter-spacing:1px}
.hero-art{position:absolute;left:110px;top:40px;width:560px;height:330px;border-radius:0 0 220px 220px;background:radial-gradient(circle at 50% 45%,#cbe9dc 0%,#b6ddd0 55%,#e3f3ec 100%)}
.title{position:absolute;left:110px;top:395px;text-align:center;width:420px}
.title-sub{font-size:46px;font-weight:800;color:var(--teal);letter-spacing:1px;line-height:1.2}
.title-main{font-size:84px;font-weight:800;color:var(--teal-dark);line-height:1.1;letter-spacing:4px;white-space:nowrap}
.no-reserve{display:inline-block;margin-top:8px;background:var(--teal);color:var(--white);font-size:24px;font-weight:700;padding:6px 28px;border-radius:24px;letter-spacing:2px}
.start-date{position:absolute;left:550px;top:385px;width:250px;height:250px;border-radius:50%;background:var(--white);border:6px solid var(--mint);display:flex;flex-direction:column;align-items:center;justify-content:center;color:var(--teal-dark);font-weight:800;white-space:nowrap;line-height:1.3}
.start-date .line1{font-size:18px}
.start-date .date{font-size:30px;color:var(--red)}
.start-date .label{font-size:30px}
.notes{position:absolute;left:70px;top:648px;width:706px;height:200px;background:var(--white);border-radius:16px;padding:18px 26px;list-style:none}
.notes li{position:relative;padding-left:22px;font-size:16px;font-weight:500;line-height:1.8}
.notes li::before{content:"";position:absolute;left:0;top:9px;width:12px;height:12px;background:var(--teal)}
.notes em{font-style:normal;color:var(--red);font-weight:700}
.nurse-art{position:absolute;left:680px;top:745px;width:80px;height:103px;border-radius:40px 40px 0 0;background:linear-gradient(180deg,#bfe3d6,#8fcdb9)}
.fee-row{position:absolute;left:40px;width:620px;display:flex;gap:12px}
.fee-row.senior{top:862px;height:180px}
.fee-row.general{top:1056px;height:124px}
.target{width:270px;background:var(--blue-panel);border-radius:12px;padding:12px 16px;font-size:26px;font-weight:700;line-height:1.3;color:var(--teal-dark);white-space:nowrap}
.target .note{display:block;font-size:12px;font-weight:500;line-height:1.5;color:var(--ink);margin-top:6px;white-space:normal}
.fee{flex:1;background:var(--white);border-radius:12px;padding:14px 20px;font-size:19px;font-weight:700;line-height:1.5;white-space:nowrap}
.fee .subsidy{color:var(--teal-dark)}
.fee .price{color:var(--red)}
.staff-art{position:absolute;left:678px;top:870px;width:130px;height:300px;border-radius:65px;background:linear-gradient(180deg,#bfe3d6,#8fcdb9)}
.bottom-band{position:absolute;left:0;bottom:0;width:846px;height:40px}
</style>
</head>
<body>
<div class="poster">
  <div class="hero-art" role="img" aria-label="看護師が女性の腕にワクチンを注射しているイラスト"></div>
  <div class="clinic-name">緑ヶ丘内科クリニック</div>

  <div class="title">
    <div class="title-sub">インフルエンザ</div>
    <div class="title-main">予防接種</div>
    <div class="no-reserve">予約は必要ありません</div>
  </div>

  <div class="start-date">
    <div class="line1"><span class="date">10月11日</span>(土)から</div>
    <div class="label">はじまります</div>
  </div>

  <ul class="notes">
    <li>インフルエンザに対する<em>抵抗力</em>がつくまで<em>2週間</em>かかり、その効果は<em>約5カ月間</em>持続します。</li>
    <li>2回接種をご希望の方は、1回目接種から<em>4週間後</em>に<em>2回目接種</em>を行います。</li>
    <li>新型コロナワクチンとの同時接種は出来ます。</li>
    <li>体温が<em>37.5度以上</em>、具合が悪い方は後日に接種しましょう。</li>
    <li>当院では妊婦の方も予防接種できます。</li>
  </ul>
  <div class="nurse-art" role="img" aria-label="マスクをした看護師のイラスト"></div>

  <div class="fee-row senior">
    <div class="target">65歳以上<br>60歳以上65歳未満<span class="note">心臓・腎臓・呼吸器疾患等の方<br>HIV感染による免疫不全の方</span></div>
    <div class="fee">
      <div class="subsidy">青葉市公費負担あり</div>
      <div>接種費用　<span class="price">¥1,500円</span></div>
      <div>接種回数　1回</div>
      <div>期間10月11日～12月31日</div>
    </div>
  </div>

  <div class="fee-row general">
    <div class="target">上記以外の方<br>13歳以上65歳未満</div>
    <div class="fee">
      <div>接種費用　1回目<span class="price">¥4,000円</span></div>
      <div>　　　　　2回目<span class="price">¥3,000円</span></div>
      <div>期間10月11日～</div>
    </div>
  </div>

  <div class="staff-art" role="img" aria-label="白衣の医師のイラスト"></div>

  <svg class="bottom-band" viewBox="0 0 846 40" preserveAspectRatio="none" aria-hidden="true">
    <path d="M0 22 Q211 2 423 22 T846 22 V40 H0 Z" fill="#a9dcc9"/>
  </svg>
</div>
</body>
</html>
```